Flyer Design

I need a nice professional flyer design to use for advertising my lawn/snow removal business. Flyers I am using are 5.47"x4.21". I've attached a flyer I found online that I liked. Just wanting something creative and professional. The images of the logos I attached are of the original logo design, and the new color design we are using. There is also a mockup of our tshirt design to give you an idea of the actual color on the tshirt, since the jpeg logo isn't exactly accurate on color.
Things I need on the flyer in no particular order:
"Snow is coming"
"Don't Wait Until It's TOO LATE!"
"Free Estimates"
Services offered
"Commercial/Residential"
"Snow Plowing"
"Snow Blowing"
"Snow Shoveling"
"Ice Removal"
"Salting/Sanding"
"Fully Licensed and Insured"
"Available and ON CALL 24/7"
"Seasonal Packages Available"
"CALL NOW TO RESERVE"

```html
<!DOCTYPE html>
<html lang="en">
<head>
<meta charset="utf-8">
<title>Snow Is Coming – Snow Removal Flyer</title>
<link rel="stylesheet" href="https://fonts.googleapis.com/css2?family=Arvo:wght@400;700&family=Roboto+Condensed:wght@400;700&display=swap">
<style>
  :root {
    --sky-dark: #2f3d52;
    --sky-mid: #5d6d84;
    --plow-red: #d7261e;
    --plow-deep: #9e1510;
    --snow: #f4f5f7;
    --slate: #4a5a70;
    --ink: #2b2f36;
    --rule: #b9c0c9;
    --headline-red: #e0231b;
    --cream: #f3ead8;
    --white: #ffffff;
  }
  * { margin: 0; padding: 0; box-sizing: border-box; }
  html, body { width: 924px; height: 1200px; overflow: hidden; background: #e6e6e6; }
  .flyer {
    position: relative;
    width: 924px;
    height: 1200px;
    overflow: hidden;
    background: var(--snow);
    font-family: "Roboto Condensed", "Arial Narrow", sans-serif;
  }
  .hero-photo {
    position: absolute;
    inset: 0;
    background:
      radial-gradient(ellipse 300px 200px at 462px 480px, rgba(255,255,255,0.35), transparent 70%),
      linear-gradient(180deg,
        var(--sky-dark) 0%,
        var(--sky-mid) 30%,
        #8a919c 40%,
        var(--plow-red) 44%,
        var(--plow-deep) 55%,
        var(--plow-red) 60%,
        #e9eaed 66%,
        var(--snow) 72%,
        var(--snow) 100%);
  }
  .title-banner {
    position: absolute;
    left: 99px;
    top: 46px;
    width: 723px;
    height: 202px;
    background: rgba(240, 242, 245, 0.92);
    text-align: center;
    box-shadow: 0 4px 14px rgba(0,0,0,0.25);
  }
  .headline {
    margin-top: 26px;
    font-family: "Arvo", Georgia, serif;
    font-weight: 700;
    font-size: 68px;
    line-height: 1;
    color: var(--headline-red);
    letter-spacing: -1px;
  }
  .banner-rule {
    width: 250px;
    height: 2px;
    margin: 20px auto 16px;
    background: var(--rule);
  }
  .tagline {
    font-family: "Arvo", Georgia, serif;
    font-size: 30px;
    color: #3a4250;
    letter-spacing: 1px;
  }
  .tagline .flake { color: #7d8796; font-size: 26px; margin: 0 14px; }
  .estimate-badge {
    position: absolute;
    left: 659px;
    top: 446px;
    width: 224px;
    height: 224px;
  }
  .services-bar {
    position: absolute;
    left: 96px;
    top: 736px;
    width: 732px;
    height: 71px;
    background: var(--slate);
    display: flex;
    align-items: center;
    justify-content: center;
    gap: 30px;
    color: var(--white);
    font-family: "Arvo", Georgia, serif;
    font-size: 40px;
  }
  .services-bar .bar-rule { width: 90px; height: 2px; background: rgba(255,255,255,0.5); }
  .service-list {
    position: absolute;
    left: 104px;
    top: 820px;
    width: 724px;
    display: grid;
    grid-template-columns: 333px 336px;
    column-gap: 55px;
    list-style: none;
  }
  .service-list li {
    height: 54px;
    display: flex;
    align-items: center;
    border-bottom: 3px solid var(--rule);
    font-size: 25px;
    color: var(--ink);
    text-transform: uppercase;
  }
  .service-list li::before {
    content: "";
    width: 8px; height: 8px;
    border-radius: 50%;
    background: var(--plow-red);
    margin-right: 16px;
  }
  .feature-boxes {
    position: absolute;
    left: 96px;
    top: 1000px;
    width: 732px;
    display: flex;
    justify-content: space-between;
  }
  .feature-box {
    width: 236px;
    height: 79px;
    background: var(--slate);
    color: var(--white);
    font-weight: 700;
    font-size: 20px;
    line-height: 1.15;
    text-transform: uppercase;
    display: flex;
    align-items: center;
    justify-content: center;
    text-align: center;
  }
  .call-to-action {
    position: absolute;
    left: 96px;
    top: 1104px;
    width: 732px;
    height: 64px;
    border-top: 3px solid var(--rule);
    border-bottom: 3px solid var(--rule);
    display: flex;
    align-items: center;
    justify-content: center;
    font-family: "Arvo", Georgia, serif;
    font-size: 46px;
    color: var(--headline-red);
    letter-spacing: 1px;
  }
  .call-to-action .dot { font-size: 30px; margin: 0 22px; }
</style>
</head>
<body>
<main class="flyer">
  <div class="hero-photo" role="img" aria-label="Photo of a pickup truck with headlights on and a red snow plow blade pushing through falling snow"></div>

  <header class="title-banner">
    <h1 class="headline">SNOW IS COMING</h1>
    <div class="banner-rule"></div>
    <p class="tagline"><span class="flake">❄</span>DON'T WAIT TILL IT'S TOO LATE!<span class="flake">❄</span></p>
  </header>

  <svg class="estimate-badge" viewBox="0 0 224 224" aria-label="Free estimates">
    <g transform="rotate(-10 112 112)">
      <circle cx="112" cy="112" r="110" fill="var(--cream)"/>
      <circle cx="112" cy="112" r="98" fill="var(--plow-red)"/>
      <circle cx="112" cy="112" r="90" fill="none" stroke="var(--cream)" stroke-width="2"/>
      <text x="112" y="112" text-anchor="middle" font-family="Roboto Condensed, sans-serif" font-weight="700" font-size="62" fill="#ffffff">FREE</text>
      <text x="112" y="146" text-anchor="middle" font-family="Arvo, serif" font-weight="700" font-size="20" fill="#ffffff" letter-spacing="1">ESTIMATES</text>
    </g>
  </svg>

  <h2 class="services-bar"><span class="bar-rule"></span>SERVICES OFFERED<span class="bar-rule"></span></h2>

  <ul class="service-list">
    <li>Commercial/Residential</li>
    <li>Snow Shoveling</li>
    <li>Snow Plowing</li>
    <li>Ice Removal</li>
    <li>Snow Blowing</li>
    <li>Salting/Sanding</li>
  </ul>

  <section class="feature-boxes">
    <div class="feature-box">Fully Licensed<br>and Insured</div>
    <div class="feature-box">Available<br>and On Call 24/7</div>
    <div class="feature-box">Seasonal Packages<br>Available</div>
  </section>

  <p class="call-to-action"><span class="dot">•</span>CALL NOW TO RESERVE<span class="dot">•</span></p>
</main>
</body>
</html>
```